Technikgewinnspiel
Zielgruppe
Technikfans, eher Männer
Aufgabenstellung
Design für ein Gewinnspiel bei dem es wechselnde Technikpreise zu gewinnen gibt.
Menüpunkte: Startseite, Teilnahmebedingungen, Preisdetails, Teilnehmen, Datenschutz.
Es soll eine Intro-Seite auf der der Preis groß heraus gestellt ist gestaltet werden mit den entsprechenden Menüpunkten sowie eine Template-Seite in der wir dann alle notwendigen Inhalte einfügen können. Von der Gestaltung her seid Ihr frei. Ich brauche dann nur etwas, wo ich dann von Monat zu Monat oder auch nur alle 3 Monate einen Preis austauschen kann. Also am besten vielleicht eine Frau oder irgendwas welches einen Preis "präsentiert" - vorzugsweise in
einem Rahmen wo der Hintergrund weiß ist (da die meisten Grafiken einen weißen Hintergrund haben) mit dem Nebentext "Dies ist Ihr aktueller Gewinn". Oder als Alternative Idee einen aufgehenden Vorhang wo der Preis dann dargestellt wird oder so. Als Größe für die austauschbare Preisgrafik reicht mir ca. 300x300 Pixel und vielleicht eine Möglichkeit einen Text unterzubringen wie "3 x Quorvo Tablo".
Gewinnspiel von uns finden Sie auf www.pokalgasse.de damit Sie sich ein Bild über die bisherigen Gewinnspiele machen können, wobei wir bisher keines haben mit austauschbaren Grafiken.
WICHTIG: Es soll nur die Eingangsseite und eine Template Seite erstellt werden. Die komplette Programmierung bzw. Füllung mit Inhalten wird von uns gemacht! Für die Templateseite wäre eine Breite von 500 Pixeln oder mehr im Bereich wo wir Inhalte einfügen können wünschenswert.
„Normales altbackenes“ HTML mit Tabellen ohne großen CSS Schnick-Schnack würden wir bevorzugen da es für uns einfacher zum Bearbeiten ist.
Das Gewinnspiel wird später auf einer Subdomain laufen und hat somit keinen Domainnamen den man im Titel darstellen kann oder muss. Der Titel könnte also „Das große Technikgewinnspiel“ lauten.
Das fertige Layout soll dann als geschnittene HTML Datei mit verlinkte..

```html
<!DOCTYPE html>
<html lang="de">
<head>
<meta charset="utf-8">
<title>Das große Technikgewinnspiel</title>
<link rel="stylesheet" href="https://fonts.googleapis.com/css2?family=Open+Sans:wght@300;400;600;700&display=swap">
<style>
  :root {
    --bg-dark: #141414;
    --bg-mid: #262626;
    --title-bold: #6f6f6f;
    --title-light: #8c8c8c;
    --panel-top: #2a2a2a;
    --panel-bottom: #0b0b0b;
    --menu-text: #d6d6d6;
    --accent-gold: #c8923b;
    --body-text: #a9a9a9;
    --footer-link: #9a9a9a;
    --button-light: #7fd4f3;
    --button-mid: #2fa9dc;
    --button-dark: #17749f;
    --button-text: #1b2a33;
    --badge-blue: #2b6fa6;
  }
  * { margin: 0; padding: 0; box-sizing: border-box; }
  html, body { width: 1200px; height: 937px; overflow: hidden; }
  body {
    position: relative;
    font-family: "Open Sans", Arial, sans-serif;
    background: radial-gradient(ellipse at 55% 40%, var(--bg-mid) 0%, var(--bg-dark) 75%);
  }
  .hero-photo {
    position: absolute; left: 112px; top: 86px; width: 330px; height: 724px; z-index: 0;
    border-radius: 48% 44% 40% 46% / 26% 28% 32% 36%;
    background: radial-gradient(ellipse at 50% 42%, #a4324a 0%, #9a3550 28%, #7e9cc0 58%, #d8d8d8 85%, #eeeeee 100%);
    box-shadow: 0 0 30px rgba(255,255,255,.35);
  }
  .headline { position: absolute; left: 0; top: 0; z-index: 2; }
  .headline-main {
    position: absolute; left: 522px; top: 163px;
    font-size: 82px; font-weight: 700; letter-spacing: 0;
    color: var(--title-bold); white-space: nowrap; line-height: 1;
  }
  .headline-sub {
    position: absolute; left: 497px; top: 247px;
    font-size: 56px; font-weight: 400; letter-spacing: -0.5px;
    color: var(--title-light); white-space: nowrap; line-height: 1;
  }
  .stage {
    position: absolute; left: 385px; top: 320px; width: 693px; height: 312px; z-index: 1;
    border-radius: 8px;
    background: linear-gradient(180deg, var(--panel-top) 0%, #151515 40%, var(--panel-bottom) 100%);
    box-shadow: 0 6px 18px rgba(0,0,0,.7), inset 0 1px 0 rgba(255,255,255,.12);
  }
  .main-nav {
    position: absolute; left: 0; top: 0; width: 100%; height: 57px;
    border-bottom: 1px solid #000;
    box-shadow: 0 1px 0 rgba(255,255,255,.06);
    display: flex; justify-content: flex-end; align-items: center; gap: 20px;
    padding-right: 22px;
  }
  .main-nav a {
    color: var(--menu-text); text-decoration: none; font-size: 13px;
    display: flex; align-items: center; gap: 5px;
  }
  .main-nav a::before { content: "›"; color: #888; font-size: 14px; }
  .prize-heading {
    position: absolute; left: 243px; top: 74px;
    font-size: 34px; line-height: 33px; font-weight: 400;
    color: var(--accent-gold); letter-spacing: -0.5px;
  }
  .prize-text {
    position: absolute; left: 35px; top: 159px; width: 450px;
    font-size: 12.5px; line-height: 17px; color: var(--body-text);
  }
  .footer-nav {
    position: absolute; left: 65px; top: 230px;
    display: flex; gap: 18px;
  }
  .footer-nav a { color: var(--footer-link); text-decoration: none; font-size: 12.5px; }
  .slider-controls { position: absolute; left: 323px; top: 252px; }
  .prize-image {
    position: absolute; left: 498px; top: 78px; width: 164px; height: 210px;
    border-radius: 12px;
    border: 3px solid #e6e6e6;
    background: linear-gradient(180deg, #1a2f55 0%, #7d8fa6 45%, #5b5240 65%, #2e3c48 100%);
    box-shadow: 0 0 0 6px #111, 0 0 14px rgba(255,255,255,.25);
  }
  .new-badge {
    position: absolute; left: 483px; top: 72px; width: 56px; height: 56px;
    border-radius: 50%;
    background: radial-gradient(circle at 40% 35%, #4a90c9, var(--badge-blue));
    border: 2px dashed #6aa9dc;
    color: #e9f4ff; font-size: 15px; font-weight: 600;
    display: flex; align-items: center; justify-content: center;
  }
  .cta-button {
    position: absolute; left: 677px; top: 651px; width: 396px; height: 56px; z-index: 1;
    border-radius: 28px;
    background: linear-gradient(180deg, var(--button-light) 0%, var(--button-mid) 50%, var(--button-dark) 100%);
    box-shadow: 0 0 0 2px #0d4f6e, 0 3px 8px rgba(0,0,0,.6);
    display: flex; align-items: center; justify-content: center;
    font-size: 33px; font-weight: 400; letter-spacing: 0.5px;
    color: var(--button-text); text-decoration: none;
    text-shadow: 0 1px 0 rgba(255,255,255,.35);
  }
</style>
</head>
<body>
  <div class="hero-photo" role="img" aria-label="Foto: springende junge Frau in rotem Top und Jeans mit weißem Lichtschein"></div>

  <header class="headline">
    <h1 class="headline-main">DAS GROSSE</h1>
    <p class="headline-sub">TECHNIKGEWINNSPIEL</p>
  </header>

  <section class="stage">
    <nav class="main-nav">
      <a href="#">Teilnahmebedingungen</a>
      <a href="#">Teilnehmen</a>
      <a href="#">Preisdetails</a>
      <a href="#">Datenschutz</a>
    </nav>

    <h2 class="prize-heading">Tolle Preise<br>zu gewinnen!</h2>
    <p class="prize-text">Lorem ipsum dolor sit amet, consectetuer adipiscing elit. Aenean commodo ligula eget dolor. Aenean massa. Cum sociis natoque penatibus et magnis dis parturient montes, nascetur ridiculus mus. Donec quam felis, ultricies nec</p>

    <nav class="footer-nav">
      <a href="#">Impressum</a>
      <a href="#">Kontakt</a>
    </nav>

    <svg class="slider-controls" width="82" height="32" viewBox="0 0 82 32" aria-label="Vor und zurück">
      <circle cx="16" cy="16" r="14" fill="#1a1a1a" stroke="#3a3a3a"/>
      <path d="M18 10 L12 16 L18 22" fill="none" stroke="#555" stroke-width="2"/>
      <circle cx="66" cy="16" r="14" fill="#1a1a1a" stroke="#3a3a3a"/>
      <path d="M64 10 L70 16 L64 22" fill="none" stroke="#555" stroke-width="2"/>
    </svg>

    <div class="prize-image" role="img" aria-label="Preisbild: Tablet-Computer mit Startbildschirm"></div>
    <div class="new-badge">NEW!</div>
  </section>

  <a class="cta-button" href="#">JETZT TEILNEHMEN</a>
</body>
</html>
```